Billboard for personal injury chiropractors office

We are a personal injury chiropractor clinic.
I need a Billboard with the company name as the dominating factor. Also a smaller picture or 2 of something creative, like a car accident or an arm in a cast off to the sides.
We Like something Clean and Simple and Eye Catching. Please make the picture Small and Off To The Side. The MAIN FOCUS areas are the… name Pell Chiropractic Clinic
At the top CAR ACCIDENT INJURY?
AND at the bottom our number 581-47-TORSO.
Dr.Marla T. Pell in bold somewhere with the word chiropractor under the doctors name in a text.

Im open to red lettering on white backgrounds, red on yellow backgrounds and I'm also open to reds blues white and yellow. I'd prefer yellow if used be across the bottom.

I am uploading a very rough draft of what we are after along with a screenshot of the tv commercial showing the yellow

DO NOT USE THE LOGO ON THE COMMERCIAL. I JUST WANT THE NAME TYPED LIKE ON SAMPLE BILLBOARD.

Industry/Entity Type

Chiropractic

Colors
0054AA
0677BA
7BADD7
CADEEF
E8F1F8
FFF300
FFF600
FEFA6F
FFFEC7
FFFEE8
EB3D1F
EC4F4E
F09395
F8D3D4
FCEDEE

Requirements
Must have
• Eye catching ,bold

```html
<!DOCTYPE html>
<html lang="en">
<head>
<meta charset="utf-8">
<title>Pell Chiropractic Clinic – Billboard</title>
<link href="https://fonts.googleapis.com/css2?family=Bebas+Neue&family=Montserrat:wght@500;700;800&display=swap" rel="stylesheet">
<style>
  :root {
    --stage: #a6a6a6;
    --board-red: #b5100c;
    --accent-yellow: #fad20f;
    --band-black: #0a0a0a;
    --title-white: #ffffff;
    --photo-shirt: #d9d9d9;
    --photo-skin: #c9977c;
    --photo-car-dark: #2b2f36;
    --photo-car-mid: #5a6068;
  }
  * { margin: 0; padding: 0; box-sizing: border-box; }
  html, body { width: 1200px; height: 1200px; overflow: hidden; }
  body {
    background: var(--stage);
    display: flex;
    align-items: center;
    justify-content: center;
  }
  .billboard {
    position: relative;
    width: 1100px;
    height: 367px;
    background: var(--board-red);
    overflow: hidden;
    box-shadow: 0 10px 18px rgba(0,0,0,0.35);
  }
  .photo-injured-arm {
    position: absolute;
    left: 0; top: 0;
    width: 270px; height: 284px;
    background: linear-gradient(135deg, var(--photo-shirt) 0%, #f2f2f2 45%, var(--photo-skin) 75%, #e8e8e8 100%);
  }
  .photo-crashed-car {
    position: absolute;
    left: 790px; right: 0;
    top: 66px; height: 218px;
    background: linear-gradient(160deg, var(--photo-car-mid) 0%, var(--photo-car-dark) 55%, #1a1c20 100%);
    clip-path: polygon(90px 28px, 200px 0, 310px 0, 310px 218px, 0 218px, 10px 110px);
  }
  .speed-streak {
    position: absolute;
    left: 620px; top: 268px;
    width: 190px; height: 16px;
    background: linear-gradient(90deg, rgba(255,120,120,0) 0%, rgba(255,120,120,0.35) 100%);
  }
  .headline {
    position: absolute;
    left: 549px;
    top: 30px;
    transform: translateX(-50%);
    text-align: center;
    font-family: "Bebas Neue", sans-serif;
    line-height: 1;
    white-space: nowrap;
  }
  .clinic-name {
    color: var(--title-white);
    font-size: 66px;
    font-weight: 400;
    letter-spacing: 0.3px;
  }
  .question {
    color: var(--accent-yellow);
    font-size: 66px;
    margin-top: 10px;
  }
  .question span { display: block; margin-top: 6px; }
  .bottom-band {
    position: absolute;
    left: 0; bottom: 0;
    width: 100%; height: 83px;
  }
  .bottom-band svg { position: absolute; inset: 0; }
  .doctor-name {
    position: absolute;
    left: 18px; top: 0;
    height: 83px;
    display: flex;
    align-items: center;
    font-family: "Montserrat", sans-serif;
    font-size: 28px;
    white-space: nowrap;
  }
  .doctor-name .initials { color: var(--accent-yellow); font-weight: 700; }
  .doctor-name .surname { color: var(--title-white); font-weight: 800; margin-left: 8px; }
  .doctor-name .title { color: var(--title-white); font-weight: 500; margin-left: 8px; }
  .phone-number {
    position: absolute;
    left: 580px; right: 0;
    top: 0; height: 83px;
    display: flex;
    align-items: center;
    justify-content: center;
    font-family: "Montserrat", sans-serif;
    font-weight: 800;
    font-size: 48px;
    color: var(--band-black);
    letter-spacing: 0.5px;
    white-space: nowrap;
  }
</style>
</head>
<body>
  <div class="billboard">
    <div class="photo-injured-arm" role="img" aria-label="Photo of a man in a white t-shirt with a bandaged arm"></div>
    <div class="speed-streak"></div>
    <div class="photo-crashed-car" role="img" aria-label="Photo of a dark car with a crushed front end after a crash"></div>

    <div class="headline">
      <h1 class="clinic-name">PELL CHIROPRACTIC CLINIC</h1>
      <p class="question">AT THE TOP<span>CAR ACCIDENT INJURY?</span></p>
    </div>

    <div class="bottom-band">
      <svg width="1100" height="83" viewBox="0 0 1100 83" preserveAspectRatio="none" aria-hidden="true">
        <rect x="0" y="0" width="1100" height="83" fill="var(--accent-yellow)"/>
        <polygon points="0,0 556,0 535,83 0,83" fill="var(--band-black)"/>
      </svg>
      <div class="doctor-name">
        <span class="initials">DR.MARLA T.</span><span class="surname">Pell</span><span class="title">Chiropractor</span>
      </div>
      <div class="phone-number">581-47-TORSO</div>
    </div>
  </div>
</body>
</html>
```